Business card - Kestrel Bay Framing

Design a business card utilizing the given logo.
colors we like: Black, greys, Teal, blues.
Tri color card, horizontal orientation likely
Logo and name likely best on top.
Info on card:

Dennis Harcourt
#5 - 1845 Larchmont Way
Surrey, B.C. V7T 3K2

604.555.0193
dennisharcourt@telvane.ca

Slogan: "Building Dreams"

We are a construction company that specializes in new home construction on the West coast of BC Canada. Bay Framing designs of high end homes.

```html
<!DOCTYPE html>
<html lang="en">
<head>
<meta charset="utf-8">
<title>Kestrel Bay Framing – Business Card</title>
<link rel="stylesheet" href="https://fonts.googleapis.com/css2?family=Open+Sans:wght@400;700&display=swap">
<style>
  :root {
    --backdrop: #4a3222;
    --card-white: #ffffff;
    --ink-black: #000000;
    --ink-dark: #1c1c1c;
    --ink-grey: #8a8a8a;
    --mark-faint: #e6e6e6;
    --rule-grey: #6a6a6a;
  }
  * { margin: 0; padding: 0; box-sizing: border-box; }
  html, body {
    width: 1200px; height: 900px; overflow: hidden;
    background: var(--backdrop);
    font-family: "Open Sans", Arial, sans-serif;
  }
  .canvas { position: relative; width: 1200px; height: 900px; }

  .card { position: absolute; box-shadow: 0 4px 14px rgba(0,0,0,.45); overflow: hidden; }

  /* Front */
  .card-front {
    left: 52px; top: 35px; width: 703px; height: 413px;
    background: var(--card-white);
  }
  .slogan-strip {
    position: absolute; left: 0; top: 0; width: 53px; height: 100%;
    background: var(--ink-black);
  }
  .slogan {
    position: absolute; left: 26px; top: 250px;
    transform: translate(-50%, -50%) rotate(-90deg);
    white-space: nowrap;
    color: var(--card-white);
    font-size: 16px; letter-spacing: 3px;
  }
  .brand {
    position: absolute; left: 70px; top: 40px;
    display: flex; align-items: center;
  }
  .brand-dot {
    width: 92px; height: 92px; border-radius: 50%;
    background: var(--ink-dark);
  }
  .brand-rule {
    width: 2px; height: 90px; margin: 0 30px;
    background: var(--rule-grey);
  }
  .brand-name {
    color: var(--ink-dark); font-weight: 400; text-transform: uppercase;
    line-height: 1;
  }
  .brand-name .line-main { display: block; font-size: 58px; letter-spacing: 1px; }
  .brand-name .line-sub { display: block; font-size: 22px; letter-spacing: 2px; margin-top: 4px; text-align: right; }

  .faint-mark {
    position: absolute; left: 460px; top: 187px;
    width: 232px; height: 232px; border-radius: 50%;
    background: var(--mark-faint);
  }

  .person { position: absolute; left: 68px; top: 176px; }
  .person-name { font-size: 23px; font-weight: 700; color: var(--ink-dark); line-height: 1.2; }
  .person-title { font-size: 17px; color: var(--ink-grey); line-height: 1.3; }

  .address {
    position: absolute; left: 68px; top: 266px;
    font-size: 18px; line-height: 26px; color: var(--ink-dark);
  }
  .contact {
    position: absolute; left: 68px; top: 341px;
    list-style: none; font-size: 18px; color: var(--ink-dark);
  }
  .contact li { display: flex; align-items: center; height: 31px; }
  .contact svg { width: 17px; height: 17px; margin-right: 10px; }

  /* Back */
  .card-back {
    left: 468px; top: 467px; width: 705px; height: 413px;
    background: var(--ink-black);
    display: flex; align-items: center; justify-content: center; gap: 24px;
  }
  .back-dot {
    width: 60px; height: 60px; border-radius: 50%;
    background: var(--card-white);
  }
  .back-name {
    color: var(--card-white); font-size: 34px; font-weight: 400;
    letter-spacing: 2px; text-transform: uppercase;
  }
</style>
</head>
<body>
<main class="canvas">

  <section class="card card-front" aria-label="Business card front">
    <div class="slogan-strip"><span class="slogan">Building Dreams</span></div>

    <div class="faint-mark" aria-hidden="true"></div>

    <header class="brand">
      <div class="brand-dot" aria-hidden="true"></div>
      <div class="brand-rule" aria-hidden="true"></div>
      <h1 class="brand-name">
        <span class="line-main">Kestrel</span>
        <span class="line-sub">Bay Framing</span>
      </h1>
    </header>

    <div class="person">
      <p class="person-name">Dennis Harcourt</p>
      <p class="person-title">CEO</p>
    </div>

    <address class="address" style="font-style: normal;">
      #5 - 1845 Larchmont Way<br>
      Surrey, B.C. V7T 3K2
    </address>

    <ul class="contact">
      <li>
        <svg viewBox="0 0 16 16" aria-hidden="true">
          <rect x="1" y="2" width="4" height="13" rx="1" fill="#1c1c1c"/>
          <rect x="6" y="4" width="9" height="11" rx="1" fill="none" stroke="#1c1c1c" stroke-width="1.5"/>
          <rect x="8" y="6" width="5" height="2" fill="#1c1c1c"/>
          <rect x="8" y="10" width="1.5" height="1.5" fill="#1c1c1c"/>
          <rect x="11" y="10" width="1.5" height="1.5" fill="#1c1c1c"/>
          <rect x="8" y="12.5" width="1.5" height="1.5" fill="#1c1c1c"/>
          <rect x="11" y="12.5" width="1.5" height="1.5" fill="#1c1c1c"/>
        </svg>
        604.555.0193
      </li>
      <li>
        <svg viewBox="0 0 16 16" aria-hidden="true">
          <rect x="1.5" y="3.5" width="13" height="9" fill="none" stroke="#1c1c1c" stroke-width="1.2"/>
          <path d="M1.5 3.5 L8 9 L14.5 3.5" fill="none" stroke="#1c1c1c" stroke-width="1.2"/>
        </svg>
        dennisharcourt@telvane.ca
      </li>
    </ul>
  </section>

  <section class="card card-back" aria-label="Business card back">
    <div class="back-dot" aria-hidden="true"></div>
    <p class="back-name">Kestrel Bay Framing</p>
  </section>

</main>
</body>
</html>
```